RT Venture Website (professional site for investors and funds)

We want to make a website for an Holding Company that owns other companies' shares in different fields. RT is the name of the holding.
We still do not have a logo or preferred colors for the company. The company, through this website, will send a clear message: it's not important where we are, it's important what we do but more than that why we do what we do.
We search for inspiration in a simple layout because we want that the user feels comfortable and guided while exploring it. The content of the website aspire to be very impressive through one or more background images.

Below, the structure of the pages explained shortly.
To learn more, we have attached a draft of the website.

Home: page with a huge backround image that fill the whole page (maybe is better to merge the navbar with the image top color?).
About: with the same huge background image, we explain which are our fields.
Why: with the same huge background image, we explain which is our why.
Projects: dropdown list with project 1, project 2, project 3. If clicked, a box like about/why pops up in order to explain projects in detail.

Target Market(s)

Investors, Entrepreneurs

Industry/Entity Type

It Company

Number of Pages Required

4 page

Font styles to use
Sans Serif

Requirements
Must have
• An idea for the background image (color and design)
• Menu
• Page layout for about/why/projects
Nice to have
• Tips for color to use in this design
Should not have
• Complicated stuff

```html
<!DOCTYPE html>
<html lang="en">
<head>
<meta charset="utf-8">
<title>RT Venture</title>
<link rel="stylesheet" href="https://fonts.googleapis.com/css2?family=Open+Sans:wght@300;400;600;700&display=swap">
<style>
:root{
  --accent:#2f8ce0;
  --accent-dark:#1e6fc2;
  --white:#ffffff;
  --text-light:#e6eef8;
  --text-dim:#9fc6f2;
  --night-top:#5f7fa3;
  --night-mid:#2b3d5c;
  --night-low:#0e1521;
  --desk-dark:#0d0e12;
  --desk-warm:#5a3c22;
  --sky-deep:#0d3fa8;
  --sky-bright:#2a7de6;
  --snow:#c9d3df;
  --field-sky:#3d7fc0;
  --field-light:#a9c8e4;
  --grass:#22461c;
  --footer-text:#444b55;
  --footer-line:#e2e6ea;
}
*{box-sizing:border-box;margin:0;padding:0}
html,body{width:1200px;height:2799px;overflow:hidden}
body{font-family:"Open Sans",Arial,sans-serif;color:var(--white);background:var(--white);position:relative}
.section{position:absolute;left:0;width:1200px;overflow:hidden}
.backdrop{position:absolute;inset:0}
.content{position:absolute;left:248px;width:704px}

/* hero */
.hero{top:0;height:685px}
.hero .backdrop{background:linear-gradient(180deg,var(--night-top) 0%,#4a6a92 18%,var(--night-mid) 38%,#1b2538 60%,var(--night-low) 100%)}
.hero .glow{position:absolute;left:0;right:0;top:260px;height:240px;background:radial-gradient(ellipse at 50% 40%,rgba(255,190,230,.28),rgba(120,160,220,.12) 45%,transparent 70%)}
.brand{position:absolute;left:248px;top:22px;font-size:34px;font-weight:600;color:var(--sky-bright);letter-spacing:1px}
.nav{position:absolute;left:756px;top:28px;display:flex;align-items:center;gap:14px;font-size:11px}
.nav a{color:var(--white);text-decoration:none}
.nav .active{background:var(--accent);padding:5px 14px;border-radius:12px}
.nav .caret{font-size:8px;margin-left:3px}
.dropdown{position:absolute;left:877px;top:56px;width:100px;background:rgba(150,180,215,.55);border-radius:3px;padding:8px 8px 10px;font-size:9px}
.dropdown li{list-style:none;padding:5px 8px;border-radius:9px;color:var(--white)}
.dropdown li.current{background:var(--accent)}
.hero-title{position:absolute;top:160px;left:0;width:1200px;text-align:center;font-size:23px;font-weight:400}
.hero-sub{position:absolute;top:200px;left:380px;width:440px;text-align:center;font-size:13px;line-height:24px;font-weight:300;color:var(--text-light)}
.cta{position:absolute;top:263px;left:540px;width:68px;height:34px;border-radius:17px;background:var(--accent);font-size:7px;font-weight:700;letter-spacing:.5px;display:flex;align-items:center;justify-content:center;text-align:center;line-height:9px}
.scroll-down{position:absolute;left:568px;width:64px;height:64px;border-radius:50%;background:rgba(20,24,32,.7);display:flex;align-items:center;justify-content:center}

/* headings */
.kicker{text-align:center;font-size:7px;letter-spacing:1.5px;color:var(--text-dim);text-transform:uppercase}
.heading{text-align:center;font-size:25px;font-weight:400;margin-top:6px}
.heading-rule{width:24px;height:2px;background:var(--white);margin:8px auto 0}

/* about */
.about{top:685px;height:687px}
.about .backdrop{background:linear-gradient(160deg,#121722 0%,var(--desk-dark) 40%,#1c1a1a 65%,var(--desk-warm) 100%)}
.about .kicker{color:#3b7fc4}
.about .heading{color:var(--accent)}
.about .heading-rule{background:var(--accent)}
.fields{display:flex;gap:11px;margin-top:50px}
.field{width:227px}
.field h3{display:flex;align-items:center;gap:7px;font-size:17px;font-weight:400;color:var(--accent)}
.field p{font-size:9px;line-height:15px;color:var(--text-light);margin-top:8px}
.field .more{display:block;margin-top:10px;font-size:8px;color:var(--accent)}

/* why */
.why{top:1372px;height:685px}
.why .backdrop{background:linear-gradient(180deg,var(--sky-deep) 0%,var(--sky-bright) 35%,#3d8ff0 58%,#6f8fb0 72%,var(--snow) 82%,#303a4c 100%)}
.columns{display:flex;gap:40px;margin-top:40px}
.col{width:332px}
.col p{font-size:9px;line-height:15px;color:var(--text-light);margin-bottom:10px}
.col ul{list-style:none;margin-bottom:10px}
.col li{font-size:9px;line-height:15px;color:var(--text-dim);opacity:.75}

/* projects */
.projects{top:2057px;height:683px}
.projects .backdrop{background:linear-gradient(180deg,var(--field-sky) 0%,#6fa2cf 25%,var(--field-light) 55%,#6f9ac2 85%,var(--grass) 96%,#17320f 100%)}
.project-name{text-align:center;margin-top:30px}
.project-name h3{font-size:19px;font-weight:400;margin-top:6px}
.projects .columns{margin-top:16px}
.projects .col p{color:var(--white)}
.slider-arrow{position:absolute;top:2365px;width:14px;height:18px}

/* footer */
.footer{position:absolute;top:2740px;left:0;width:1200px;height:59px;background:var(--white);border-top:1px solid var(--footer-line)}
.copyright{position:absolute;left:248px;top:24px;font-size:8px;color:var(--footer-text)}
.copyright span{color:var(--accent)}
.social{position:absolute;left:806px;top:21px;display:flex;gap:7px}
.social li{list-style:none;width:16px;height:16px;border-radius:50%;border:1px solid var(--accent)}
</style>
</head>
<body>

<section class="section hero" id="home">
  <div class="backdrop" role="img" aria-label="Night view of a city skyline lit up below a hillside at dusk"></div>
  <div class="glow"></div>
  <div class="brand">RT</div>
  <nav class="nav">
    <a class="active" href="#home">Home</a>
    <a href="#about">About</a>
    <a href="#why">Why</a>
    <a href="#projects">Projects<span class="caret">▾</span></a>
  </nav>
  <ul class="dropdown">
    <li class="current">Wind Energy</li>
    <li>IT</li>
    <li>Consulting</li>
  </ul>
  <h1 class="hero-title">Welcome to RT Venture</h1>
  <p class="hero-sub">It's not important where we are, it's important what we do but more than that why we do what we do.</p>
  <div class="cta">LET'S GET<br>STARTED</div>
  <div class="scroll-down" style="top:548px"><svg width="22" height="12" viewBox="0 0 22 12"><path d="M1 1l10 10L21 1" fill="none" stroke="#fff" stroke-width="1.5"/></svg></div>
</section>

<section class="section about" id="about">
  <div class="backdrop" role="img" aria-label="Hands typing on a laptop keyboard at a wooden desk, wristwatch on the wrist"></div>
  <div class="content" style="top:72px">
    <p class="kicker">Learn more about us</p>
    <h2 class="heading">About Us</h2>
    <div class="fields">
      <div class="field">
        <h3><svg width="18" height="18" viewBox="0 0 18 18"><g stroke="#2f8ce0" stroke-width="1.6" stroke-linecap="round"><path d="M9 8V17"/><path d="M9 8L9 1"/><path d="M9 8L2 12"/><path d="M9 8L16 12"/></g></svg>Wind Energy</h3>
        <p>We invest in clean power producers that turn steady wind into long term value, backing teams with proven sites, sound grids and clear plans for growth.</p>
        <span class="more">Keep Reading ›</span>
      </div>
      <div class="field">
        <h3><svg width="20" height="16" viewBox="0 0 20 16"><rect x="1" y="2" width="12" height="9" fill="none" stroke="#2f8ce0" stroke-width="1.6"/><rect x="15" y="1" width="4" height="14" fill="#2f8ce0"/><path d="M4 14h6" stroke="#2f8ce0" stroke-width="1.6"/></svg>IT</h3>
        <p>Our technology holdings build software, cloud services and secure networks for firms that need reliable systems to scale fast in changing markets.</p>
        <span class="more">Keep Reading ›</span>
      </div>
      <div class="field">
        <h3><svg width="18" height="16" viewBox="0 0 18 16"><rect x="1" y="1" width="10" height="8" rx="2" fill="#2f8ce0"/><rect x="7" y="6" width="10" height="8" rx="2" fill="#6bb3f5"/></svg>Consulting</h3>
        <p>We hold stakes in advisory firms that help owners plan, finance and grow their companies with clear strategy and careful execution.</p>
        <span class="more">Keep Reading ›</span>
      </div>
    </div>
  </div>
  <div class="scroll-down" style="top:548px"><svg width="22" height="12" viewBox="0 0 22 12"><path d="M1 1l10 10L21 1" fill="none" stroke="#fff" stroke-width="1.5"/></svg></div>
</section>

<section class="section why" id="why">
  <div class="backdrop" role="img" aria-label="Deep blue sky with clouds above snow covered mountain ridges"></div>
  <div class="content" style="top:70px">
    <p class="kicker">We're simple - no surprises</p>
    <h2 class="heading">Why Us</h2>
    <div class="heading-rule"></div>
    <div class="columns" style="margin-top:28px">
      <div class="col">
        <p>We believe capital should serve people first. Every share we hold is a promise to the founders, teams and markets that trust us with their future work.</p>
        <p>We choose partners with care and stay close to them, sharing our network and our time as much as our funds.</p>
        <p>Our aim is simple: lasting companies that create value for investors, for staff and for the places where they grow.</p>
      </div>
      <div class="col">
        <p>We look past short trends and measure success in decades, not quarters, keeping our goals clear and our steps honest.</p>
        <ul>
          <li>– Long term ownership of every stake</li>
          <li>– Open reporting to all investors</li>
          <li>– Direct support for each founder</li>
          <li>– Careful risk across many fields</li>
          <li>– Growth built on real value</li>
        </ul>
        <p>Simple choices, clear results and no surprises along the way.</p>
      </div>
    </div>
  </div>
  <div class="scroll-down" style="top:542px"><svg width="22" height="12" viewBox="0 0 22 12"><path d="M1 1l10 10L21 1" fill="none" stroke="#fff" stroke-width="1.5"/></svg></div>
</section>

<section class="section projects" id="projects">
  <div class="backdrop" role="img" aria-label="Row of wind turbines on a green plain under a wide pale blue sky"></div>
  <div class="content" style="top:70px">
    <p class="kicker" style="color:#e6eef8">What we can do for you</p>
    <h2 class="heading" style="color:#111">Our Projects</h2>
    <div class="heading-rule" style="background:#111"></div>
    <div class="project-name">
      <svg width="22" height="26" viewBox="0 0 22 26"><g stroke="#111" stroke-width="2" stroke-linecap="round"><path d="M11 10V25"/><path d="M11 10L11 1"/><path d="M11 10L3 15"/><path d="M11 10L19 15"/></g></svg>
      <h3 style="color:#111">Wind Energy</h3>
    </div>
    <div class="columns">
      <div class="col">
        <p>Our first wind portfolio spans coastal and upland sites, delivering clean power to regional grids under long term supply contracts.</p>
        <p>Each farm is run by a local team with modern turbines and remote monitoring for steady output.</p>
        <p>New sites are planned with the community and assessed for nature, noise and land use.</p>
      </div>
      <div class="col">
        <p>We fund upgrades that raise capacity on existing farms while lowering upkeep cost across the fleet.</p>
        <p>Storage trials pair batteries with turbines to smooth supply in calm weather.</p>
        <p>Revenue is reinvested into new capacity and local grid links.</p>
        <p>Clean energy remains a core field for us.</p>
      </div>
    </div>
  </div>
</section>
<svg class="slider-arrow" style="left:150px" viewBox="0 0 14 18"><path d="M11 1L3 9l8 8" fill="none" stroke="#fff" stroke-width="1.5"/></svg>
<svg class="slider-arrow" style="left:1036px" viewBox="0 0 14 18"><path d="M3 1l8 8-8 8" fill="none" stroke="#fff" stroke-width="1.5"/></svg>

<footer class="footer">
  <p class="copyright">Copyright © 2017 - <span>RT Venture</span> - All Rights Reserved</p>
  <ul class="social">
    <li></li><li></li><li></li><li></li><li></li><li></li><li></li>
  </ul>
</footer>

</body>
</html>
```